Business cards and stationary for Auto Body Shop
R & T Auto Body Service Inc.
Simple
Delmor Quenivash
28476 Pellway Street
Van Nuys, CA 91411
rtautobodyinc@brivomail.com
www.rtautobody-example.com
Just the Logo I guess.
Please us this new logo.

```html
<!DOCTYPE html>
<html lang="en">
<head>
<meta charset="utf-8">
<title>R &amp; T Auto Body – Stationery</title>
<link href="https://fonts.googleapis.com/css2?family=Cinzel:wght@500&family=Open+Sans:wght@400;600&display=swap" rel="stylesheet">
<style>
:root{
  --bg:#4a3a2e;
  --paper:#ffffff;
  --ink:#1f1f1f;
  --muted:#7a7a7a;
  --faint:#ececec;
  --band-dark:#2a2a2a;
  --band-mid:#8c8c8c;
  --label:#d8cfc6;
  --flap-light:#f4f4f4;
  --flap-line:#d0d0d0;
}
*{margin:0;padding:0;box-sizing:border-box}
html,body{width:1200px;height:466px;overflow:hidden;background:var(--bg)}
.canvas{position:relative;width:1200px;height:466px;font-family:"Open Sans",Arial,sans-serif;color:var(--ink)}
.sheet{position:absolute;background:var(--paper);box-shadow:0 2px 6px rgba(0,0,0,.35);overflow:hidden}
.label{position:absolute;font-size:5px;letter-spacing:.8px;color:var(--label);text-transform:uppercase;white-space:nowrap}
.brand{display:flex;align-items:center;gap:4px;white-space:nowrap}
.brand-mark{border:1.5px solid var(--ink);border-radius:50%;flex:none}
.brand-name{font-family:"Cinzel",Georgia,serif;font-weight:500;color:var(--ink);letter-spacing:.5px}
.contact{font-size:4.5px;line-height:6.5px;color:var(--ink);white-space:nowrap}
.contact span{display:flex;align-items:center;gap:3px}
.contact i{width:3px;height:3px;background:var(--ink);border-radius:50%;display:inline-block;flex:none}
.band{position:absolute;left:0;right:0;height:8px;background:linear-gradient(90deg,var(--band-dark),var(--band-mid) 50%,var(--band-dark))}
.band-thin{position:absolute;left:0;right:0;height:2px;background:#bdbdbd}
.watermark{position:absolute;font-family:"Cinzel",Georgia,serif;font-weight:500;color:var(--faint);white-space:nowrap;line-height:1}
.footer-text{position:absolute;left:0;right:0;font-size:4px;text-align:center;color:var(--muted);letter-spacing:.5px}
</style>
</head>
<body>
<div class="canvas">

  <!-- business cards -->
  <div class="label" style="left:29px;top:139px">Stationery Concepts</div>

  <div class="sheet business-card-front" style="left:29px;top:166px;width:84px;height:50px">
    <div class="brand" style="position:absolute;left:6px;top:7px;gap:3px">
      <div class="brand-mark" style="width:10px;height:10px;border-width:1px"></div>
      <div class="brand-name" style="font-size:5px">R &amp; T Auto Body</div>
    </div>
    <div class="contact" style="position:absolute;left:6px;top:23px;font-size:3.4px;line-height:4.6px">
      Delmor Quenivash<br>Tel (818) 555-0142<br>rtautobodyinc@brivomail.com
    </div>
    <div class="band" style="bottom:3px;height:3px"></div>
  </div>
  <div class="label" style="left:29px;top:221px">Business Card Front</div>

  <div class="sheet business-card-back" style="left:29px;top:250px;width:84px;height:50px">
    <div class="brand" style="position:absolute;left:50%;top:46%;transform:translate(-50%,-50%);flex-direction:column;gap:3px">
      <div class="brand-mark" style="width:14px;height:14px;border-width:1px"></div>
      <div class="brand-name" style="font-size:4.5px">R &amp; T Auto Body</div>
    </div>
    <div class="band" style="bottom:3px;height:3px"></div>
  </div>
  <div class="label" style="left:29px;top:305px">Business Card Back</div>

  <!-- letterhead option 1 -->
  <div class="sheet letterhead" style="left:163px;top:34px;width:283px;height:357px">
    <div class="brand" style="position:absolute;left:16px;top:16px">
      <div class="brand-mark" style="width:16px;height:16px"></div>
      <div class="brand-name" style="font-size:8px">R &amp; T Auto Body</div>
    </div>
    <div class="contact" style="position:absolute;left:150px;top:12px">
      <span><i></i>28476 Pellway Street</span>
      <span><i></i>Van Nuys, CA 91411</span>
      <span><i></i>Tel (818) 555-0142</span>
      <span><i></i>rtautobodyinc@brivomail.com</span>
      <span><i></i>www.rtautobody-example.com</span>
    </div>
    <div class="watermark" style="left:50%;top:200px;transform:translateX(-50%);font-size:100px">R&amp;T</div>
    <div class="band" style="bottom:20px"></div>
    <div class="band-thin" style="bottom:14px"></div>
    <div class="footer-text" style="bottom:5px">Collision · Paint · Repair</div>
  </div>
  <div class="label" style="left:272px;top:398px">Letterhead Option 1</div>

  <!-- letterhead option 2 -->
  <div class="sheet letterhead" style="left:470px;top:34px;width:281px;height:357px">
    <div class="brand" style="position:absolute;left:50%;top:12px;transform:translateX(-50%);flex-direction:column;gap:3px">
      <div class="brand-mark" style="width:16px;height:16px"></div>
      <div class="brand-name" style="font-size:8px">R &amp; T Auto Body</div>
    </div>
    <div class="watermark" style="left:50%;top:120px;transform:translateX(-50%);font-size:95px">R&amp;T</div>
    <div class="contact" style="position:absolute;left:12px;right:12px;bottom:34px;display:flex;justify-content:space-between;font-size:3.8px">
      <span><i></i>28476 Pellway Street, Van Nuys, CA 91411</span>
      <span><i></i>rtautobodyinc@brivomail.com</span>
      <span><i></i>www.rtautobody-example.com</span>
    </div>
    <div class="band" style="bottom:20px"></div>
    <div class="band-thin" style="bottom:14px"></div>
  </div>
  <div class="label" style="left:578px;top:398px">Letterhead Option 2</div>

  <!-- envelopes -->
  <div class="sheet envelope-open" style="left:780px;top:17px;width:396px;height:115px">
    <svg width="396" height="115" viewBox="0 0 396 115" aria-hidden="true" style="position:absolute;left:0;top:0">
      <defs><linearGradient id="flapDark" x1="0" y1="0" x2="0" y2="1"><stop offset="0" stop-color="#111"/><stop offset="1" stop-color="#5a5a5a"/></linearGradient></defs>
      <path d="M0 0 H396 V36 L366 62 H30 L0 36 Z" fill="url(#flapDark)"/>
    </svg>
  </div>

  <div class="sheet envelope-flap" style="left:780px;top:140px;width:396px;height:118px">
    <svg width="396" height="118" viewBox="0 0 396 118" aria-hidden="true" style="position:absolute;left:0;top:0">
      <path d="M0 0 H396 V24 L366 50 H30 L0 24 Z" fill="var(--flap-light)" stroke="var(--flap-line)" stroke-width="1"/>
    </svg>
    <div class="brand" style="position:absolute;left:50%;top:72px;transform:translateX(-50%);gap:5px">
      <div class="brand-mark" style="width:14px;height:14px"></div>
      <div class="brand-name" style="font-size:7px">R &amp; T Auto Body</div>
    </div>
  </div>

  <div class="sheet envelope-closed" style="left:780px;top:266px;width:396px;height:118px">
    <div class="brand" style="position:absolute;left:14px;top:12px">
      <div class="brand-mark" style="width:16px;height:16px"></div>
      <div class="brand-name" style="font-size:8px">R &amp; T Auto Body</div>
    </div>
    <div class="contact" style="position:absolute;left:34px;top:32px;font-size:4px;line-height:5.5px">
      28476 Pellway Street, Van Nuys, CA 91411<br>www.rtautobody-example.com
    </div>
    <div class="band" style="bottom:14px"></div>
    <div class="band-thin" style="bottom:9px"></div>
  </div>
  <div class="label" style="left:945px;top:391px">Envelope Option 1</div>

</div>
</body>
</html>
```